Design NEW business card

We would like a business card using the colour deep red wine or dark navy blue textured background (patterned or not, open to suggestions) with a high gloss debossed rose gold/copper MT Martin Tully Jewellery business name (Provided). I have included images for your review we would like to keep our currently logo and business name on the front but you can change the layout and positioning. For the back of the card we are open to all suggestions/variations.
Industry/Entity Type
Business
Contact Information for Business Card
Use our current MT Martin Tully Jewellery logo (Provided image)
Look and feel
Each slider illustrates characteristics of the customer's brand and the style your logo design should communicate.

```html
<!DOCTYPE html>
<html lang="en">
<head>
<meta charset="utf-8">
<title>Martin Tully Jewellery – Business Card</title>
<link href="https://fonts.googleapis.com/css2?family=Montserrat:wght@400&family=Roboto:wght@400&family=Roboto+Condensed:wght@400;700&display=swap" rel="stylesheet">
<style>
  :root {
    --page-bg: #dcdcdc;
    --wine: #5a1424;
    --wine-light: #7a2236;
    --wine-dark: #3e0b17;
    --rose-gold: #d9a27f;
    --rose-gold-light: #ecc2a3;
    --rose-gold-dark: #b98063;
    --text-light: #f1e4dc;
    --text-muted: #c99a85;
    --divider: #a5705c;
  }
  html, body {
    margin: 0;
    padding: 0;
    width: 1200px;
    height: 960px;
    overflow: hidden;
    background: var(--page-bg);
  }
  .canvas {
    position: relative;
    width: 1200px;
    height: 960px;
  }
  .card {
    position: absolute;
    width: 600px;
    height: 330px;
    box-sizing: border-box;
  }
  .card--front {
    left: 314px;
    top: 113px;
    background:
      repeating-linear-gradient(45deg, rgba(255,255,255,0.025) 0 1px, transparent 1px 4px),
      repeating-linear-gradient(-45deg, rgba(0,0,0,0.05) 0 1px, transparent 1px 4px),
      linear-gradient(135deg, var(--wine-light) 0%, var(--wine) 50%, var(--wine-dark) 100%);
  }
  .card--back {
    left: 311px;
    top: 478px;
    background:
      repeating-linear-gradient(45deg, rgba(255,255,255,0.025) 0 1px, transparent 1px 4px),
      repeating-linear-gradient(-45deg, rgba(0,0,0,0.05) 0 1px, transparent 1px 4px),
      radial-gradient(ellipse 340px 230px at 50% 38%, var(--wine-light) 0%, var(--wine) 55%, var(--wine-dark) 100%);
  }
  .wordmark {
    position: absolute;
    text-align: center;
    font-family: "Montserrat", sans-serif;
    font-weight: 400;
    color: var(--rose-gold);
  }
  .wordmark__name,
  .wordmark__trade {
    display: block;
    white-space: nowrap;
  }
  .card--front .wordmark {
    left: 60px;
    top: 208px;
    width: 276px;
  }
  .card--front .wordmark__name {
    font-size: 20px;
    letter-spacing: 3px;
  }
  .card--front .wordmark__trade {
    margin-top: 6px;
    font-size: 8px;
    letter-spacing: 12px;
    padding-left: 12px;
  }
  .divider {
    position: absolute;
    left: 326px;
    top: 72px;
    width: 1px;
    height: 186px;
    background: var(--divider);
  }
  .contact {
    position: absolute;
    left: 357px;
    top: 70px;
    font-family: "Roboto", sans-serif;
    color: var(--text-light);
  }
  .contact__name {
    margin: 0;
    font-family: "Roboto Condensed", sans-serif;
    font-weight: 700;
    font-size: 21px;
    line-height: 26px;
    color: var(--rose-gold);
  }
  .contact__role {
    margin: 0;
    font-family: "Roboto Condensed", sans-serif;
    font-size: 15px;
    line-height: 20px;
    color: var(--text-muted);
  }
  .contact__address {
    margin: 12px 0 0;
    font-size: 14.5px;
    line-height: 19px;
    font-style: normal;
  }
  .contact__list {
    list-style: none;
    margin: 9px 0 0;
    padding: 0;
    font-size: 14.5px;
    line-height: 19px;
  }
  .contact__list li {
    display: flex;
    align-items: center;
  }
  .contact__icon {
    width: 13px;
    height: 13px;
    margin-right: 10px;
    fill: var(--rose-gold);
  }
  .card--back .wordmark {
    left: 206px;
    top: 200px;
    width: 250px;
    color: var(--rose-gold-light);
  }
  .card--back .wordmark__name {
    font-size: 23px;
    letter-spacing: 3.5px;
  }
  .card--back .wordmark__trade {
    margin-top: 6px;
    font-size: 9px;
    letter-spacing: 14px;
    padding-left: 14px;
  }
  .web {
    position: absolute;
    left: 0;
    top: 287px;
    width: 600px;
    text-align: center;
    font-family: "Roboto", sans-serif;
    font-size: 14px;
    letter-spacing: 6px;
    color: var(--rose-gold-light);
  }
</style>
</head>
<body>
<main class="canvas">

  <section class="card card--front" aria-label="Card front">
    <div class="wordmark">
      <span class="wordmark__name">MARTIN TULLY</span>
      <span class="wordmark__trade">JEWELLERY</span>
    </div>

    <div class="divider"></div>

    <div class="contact">
      <h1 class="contact__name">DANIEL REYES</h1>
      <p class="contact__role">CEO/FOUNDER</p>
      <address class="contact__address">214 Harbor View Road<br>Juneau, Alaska 99801</address>
      <ul class="contact__list">
        <li>
          <svg class="contact__icon" viewBox="0 0 16 16" aria-hidden="true"><path d="M3.5 1l2.5 3-1.5 1.8c.8 1.9 2.3 3.4 4.2 4.2L10.5 8.5l3 2.5-1.3 2.6C7 13.4 2.6 9 2.4 3.8z"/></svg>
          555 214 0187
        </li>
        <li>
          <svg class="contact__icon" viewBox="0 0 16 16" aria-hidden="true"><path d="M4.5 0h7a1 1 0 0 1 1 1v14a1 1 0 0 1-1 1h-7a1 1 0 0 1-1-1V1a1 1 0 0 1 1-1zm.5 2v10h6V2zm3 11a1 1 0 1 0 0 2 1 1 0 0 0 0-2z"/></svg>
          555 316 2740
        </li>
        <li>
          <svg class="contact__icon" viewBox="0 0 16 16" aria-hidden="true"><path d="M4 1h6l2 2v3H4zM1 7h14v6h-2v2H3v-2H1zm4 4v2h6v-2z"/></svg>
          555 428 9013
        </li>
        <li>
          <svg class="contact__icon" viewBox="0 0 16 16" aria-hidden="true"><path d="M1 3h14v1.2L8 9 1 4.2zm0 2.6l7 4.8 7-4.8V13H1z"/></svg>
          info@tullyjewel.com
        </li>
        <li>
          <svg class="contact__icon" viewBox="0 0 16 16" aria-hidden="true"><circle cx="8" cy="8" r="7"/><path d="M1 8h14M8 1c-2.5 2.5-2.5 11.5 0 14M8 1c2.5 2.5 2.5 11.5 0 14" stroke="#5a1424" stroke-width="1" fill="none"/></svg>
          www.tullyjewel.com
        </li>
      </ul>
    </div>
  </section>

  <section class="card card--back" aria-label="Card back">
    <div class="wordmark">
      <span class="wordmark__name">MARTIN TULLY</span>
      <span class="wordmark__trade">JEWELLERY</span>
    </div>
    <div class="web">www.tullyjewel.com</div>
  </section>

</main>
</body>
</html>
```